Creative & Professional Business Card for hair salon

We are looking to update our business cards. Our salon is creative, modern, progressive and professional and looking for a design that will reflect this.

```html
<!DOCTYPE html>
<html lang="en">
<head>
<meta charset="utf-8">
<title>Silver Lining Salon – Business Card</title>
<link href="https://fonts.googleapis.com/css2?family=Questrial&family=Lato:wght@400;700&display=swap" rel="stylesheet">
<style>
  :root{
    --stage:#2a2a2c;
    --sky-deep:#3f8fd6;
    --sky-mid:#6aaee6;
    --sky-pale:#cfe3f5;
    --cloud:#f7f9fc;
    --ink:#161616;
    --ink-soft:#2c2c2c;
    --paper:#ffffff;
  }
  *{box-sizing:border-box;margin:0;padding:0}
  html,body{width:1200px;height:900px;overflow:hidden}
  body{
    background:var(--stage);
    font-family:"Questrial",sans-serif;
    color:var(--ink);
    display:flex;flex-direction:column;align-items:center;justify-content:center;gap:44px;
  }
  .card{
    position:relative;width:640px;height:366px;border-radius:16px;overflow:hidden;
    box-shadow:0 14px 30px rgba(0,0,0,.45);
  }
  .card__sky{position:absolute;inset:0}
  .card__sky--back{
    background:
      radial-gradient(ellipse 70% 60% at 70% 70%, var(--cloud) 0 55%, transparent 75%),
      radial-gradient(ellipse 55% 50% at 15% 95%, var(--cloud) 0 50%, transparent 75%),
      linear-gradient(180deg,var(--sky-pale) 0%,#e6f0f9 45%,var(--cloud) 100%);
  }
  .card__sky--front{
    background:
      radial-gradient(ellipse 55% 60% at 85% 70%, var(--cloud) 0 45%, transparent 72%),
      radial-gradient(ellipse 60% 40% at 25% 100%, var(--cloud) 0 45%, transparent 75%),
      linear-gradient(160deg,var(--sky-deep) 0%,var(--sky-mid) 55%,#a9cfee 100%);
  }
  .content{position:absolute;inset:0}

  /* back: appointment side */
  .label{
    display:inline-block;background:var(--ink);color:var(--paper);
    font-size:17px;letter-spacing:.5px;padding:3px 12px 2px;text-transform:uppercase;
  }
  .label--small{font-size:13px;padding:2px 8px 1px}
  .appointment{position:absolute;left:0;right:0;top:34px;text-align:center}
  .fields{position:absolute;left:48px;right:48px;top:92px;font-size:17px;color:var(--ink-soft)}
  .field{display:flex;align-items:flex-end;gap:8px;margin-bottom:26px}
  .field__line{flex:1;border-bottom:2px dotted var(--ink-soft);height:1px;margin-bottom:5px}
  .field__gap{width:40px}
  .policy{position:absolute;left:60px;right:60px;top:218px;text-align:center}
  .policy__text{margin-top:10px;font-size:14px;line-height:1.4;color:var(--ink-soft)}
  .website-spaced{
    position:absolute;left:0;right:0;bottom:30px;text-align:center;
    font-family:"Lato",sans-serif;font-weight:700;font-size:12px;letter-spacing:5px;
  }

  /* front: brand side */
  .brand{position:absolute;left:46px;top:56px;color:var(--paper)}
  .brand__row{display:flex;align-items:center;gap:12px}
  .brand__dot{width:20px;height:20px;border-radius:50%;background:var(--paper)}
  .brand__name{font-size:34px;line-height:1}
  .brand__by{font-size:18px;margin:8px 0 0 32px}
  .booking{
    position:absolute;right:34px;top:150px;text-align:right;
    font-family:"Lato",sans-serif;color:var(--ink);
  }
  .booking__title{font-weight:700;font-size:14px;text-decoration:underline}
  .booking__call{font-size:15px;margin-top:4px}
  .booking__web{font-size:12px;margin-top:4px}
  .contacts{
    position:absolute;left:30px;bottom:26px;list-style:none;
    font-family:"Lato",sans-serif;font-size:14px;color:var(--ink);
  }
  .contacts li{display:flex;align-items:center;gap:8px;margin-top:5px}
  .contacts__icon{width:16px;height:16px;flex:none}
  .contacts__address{font-weight:700;font-size:15px}
</style>
</head>
<body>

  <section class="card card--back">
    <div class="card__sky card__sky--back" role="img" aria-label="Photograph of white cumulus clouds in a pale blue sky"></div>
    <div class="content">
      <div class="appointment"><span class="label">Next Appointment</span></div>
      <div class="fields">
        <div class="field"><span>Date:</span><span class="field__line"></span><span class="field__gap"></span><span>Time:</span><span class="field__line"></span></div>
        <div class="field"><span>Appointment For:</span><span class="field__line"></span></div>
      </div>
      <div class="policy">
        <span class="label label--small">Cancellation Policy</span>
        <p class="policy__text">If you are unable to keep your appointment, pl provide atleast<br>2 business days notice or full visit fee will apply.</p>
      </div>
      <p class="website-spaced">www.silverliningsalon.com.au</p>
    </div>
  </section>

  <section class="card card--front">
    <div class="card__sky card__sky--front" role="img" aria-label="Photograph of bright blue sky with billowing white clouds"></div>
    <div class="content">
      <div class="brand">
        <div class="brand__row"><span class="brand__dot"></span><span class="brand__name">Silver Lining Salon</span></div>
        <p class="brand__by">by Mia Corvetti</p>
      </div>
      <div class="booking">
        <p class="booking__title">FOR APPOINTMENT OR BOOK:</p>
        <p class="booking__call">Call 07 5550 1284</p>
        <p class="booking__web">www.silverliningsalon.com.au</p>
      </div>
      <ul class="contacts">
        <li>
          <svg class="contacts__icon" viewBox="0 0 16 16" aria-hidden="true"><circle cx="8" cy="8" r="8" fill="#161616"/><path d="M5 4.5c.6-.4 1.1-.2 1.4.4l.5 1c.2.4 0 .8-.3 1l-.4.3c.4.9 1 1.6 1.9 2l.3-.4c.3-.3.7-.4 1-.2l1 .6c.5.3.6.9.2 1.4-.7.8-1.8.9-2.8.3C6 10 5 8.9 4.4 7.5 4 6.4 4.2 5.2 5 4.5z" fill="#fff"/></svg>
          <span>07 5550 1284</span>
        </li>
        <li>
          <svg class="contacts__icon" viewBox="0 0 16 16" aria-hidden="true"><circle cx="8" cy="8" r="8" fill="#161616"/><rect x="4" y="5" width="8" height="6" rx="1" fill="#fff"/><path d="M4.3 5.4 8 8.3l3.7-2.9" stroke="#161616" stroke-width="1" fill="none"/></svg>
          <span>hello@silverliningsalon.com.au</span>
        </li>
        <li>
          <svg class="contacts__icon" viewBox="0 0 16 16" aria-hidden="true"><circle cx="8" cy="8" r="8" fill="#161616"/></svg>
          <span>@silverliningbymiacorvetti</span>
        </li>
        <li class="contacts__address">5/12 Harbour Lane, Seaview Qld 4573</li>
      </ul>
    </div>
  </section>

</body>
</html>
```